I would like to start a new webpage for a dating site in switzerland.
The dating site is not a escort service at all and should not transmit any type of sexual connotation.
The is more a compagnionship dating : male pay to meet ladies for some time in which they invite them for dinner, coktail, museum visit or walking or even skying. the meeting will take place in big cities in switzerland: geneva, zurich, bern, lausannes.

```html
<!DOCTYPE html>
<html lang="en">
<head>
<meta charset="utf-8">
<title>StrollTogether – Create an account</title>
<link rel="stylesheet" href="https://fonts.googleapis.com/css2?family=PT+Sans:wght@400;700&display=swap">
<style>
  :root {
    --bar-dark: #2a2a2a;
    --bar-line: #3c3c3c;
    --logo-grey: #6b6b6b;
    --rose: #de1565;
    --berry: #a8345c;
    --leaf: #5a9e12;
    --leaf-button: #5c981e;
    --panel-head: rgba(58, 56, 50, 0.92);
    --panel-body: rgba(246, 246, 238, 0.86);
    --label: #2c2c2c;
    --field-line: #8f8f86;
    --placeholder: #8a8a84;
    --footer-text: #8c8c8c;
    --meadow-top: #d3dcaa;
    --meadow-mid: #b9cf82;
    --meadow-low: #7fb33e;
    --meadow-bottom: #5f9c2a;
  }
  * { box-sizing: border-box; margin: 0; padding: 0; }
  html, body {
    width: 1200px; height: 785px; overflow: hidden;
    font-family: "PT Sans", Arial, sans-serif;
    background: var(--bar-dark);
  }
  .page { position: relative; width: 1200px; height: 785px; overflow: hidden; }

  .site-header {
    position: absolute; left: 0; top: 0; width: 1200px; height: 53px;
    background: var(--bar-dark); border-bottom: 2px solid var(--bar-line); z-index: 2;
  }
  .brand { position: absolute; left: 115px; top: 12px; display: flex; align-items: center; }
  .brand-dot { width: 32px; height: 32px; border-radius: 50%; background: var(--rose); }
  .brand-name { margin-left: 10px; font-size: 16px; color: var(--logo-grey); }
  .header-button {
    position: absolute; top: 8px; width: 93px; height: 35px; border-radius: 2px;
    color: #fff; font-size: 16px; line-height: 35px; text-align: center;
  }
  .header-button--login { left: 893px; background: var(--rose); }
  .header-button--search { left: 997px; background: var(--leaf); }

  .hero-photo {
    position: absolute; left: 0; top: 53px; width: 1200px; height: 695px;
    background: linear-gradient(180deg, var(--meadow-top) 0%, var(--meadow-mid) 40%, var(--meadow-low) 75%, var(--meadow-bottom) 100%);
  }

  .signup {
    position: absolute; left: 114px; top: 200px; width: 549px; height: 427px;
    border-radius: 6px; overflow: hidden; background: var(--panel-body);
  }
  .signup-title {
    height: 48px; background: var(--panel-head); color: #fff;
    font-size: 19px; font-weight: 400; line-height: 48px; padding-left: 28px;
  }
  .field { position: absolute; width: 227px; }
  .field-label { display: block; font-size: 14px; font-weight: 700; color: var(--label); height: 22px; }
  .field-box {
    position: relative; margin-top: 1px; height: 37px; border: 1px solid var(--field-line);
    border-radius: 3px; background: transparent; font-size: 13px; color: var(--placeholder);
    line-height: 35px; padding-left: 15px;
  }
  .field-box--select .select-arrow {
    position: absolute; right: -1px; top: -1px; width: 34px; height: 37px;
    background: var(--berry); border-radius: 0 3px 3px 0;
    display: flex; align-items: center; justify-content: center;
  }
  .register-button {
    position: absolute; left: 29px; top: 360px; width: 106px; height: 37px;
    background: var(--leaf-button); color: #fff; border-radius: 3px;
    font-size: 15px; line-height: 37px; text-align: center;
  }

  .site-footer {
    position: absolute; left: 0; top: 748px; width: 1200px; height: 37px;
    background: var(--bar-dark);
  }
  .copyright { position: absolute; left: 142px; top: 12px; font-size: 12px; color: var(--footer-text); }
</style>
</head>
<body>
<div class="page">
  <header class="site-header">
    <div class="brand">
      <span class="brand-dot"></span>
      <span class="brand-name">Logo Here</span>
    </div>
    <span class="header-button header-button--login">Login</span>
    <span class="header-button header-button--search">Search</span>
  </header>

  <div class="hero-photo" role="img" aria-label="Misty green meadow with pink wildflowers and a couple sitting together under a pink umbrella"></div>

  <section class="signup">
    <h1 class="signup-title">Create an account</h1>

    <div class="field" style="left:29px; top:77px;">
      <span class="field-label">First Name</span>
      <div class="field-box">Enter Your First Name</div>
    </div>
    <div class="field" style="left:296px; top:77px;">
      <span class="field-label">Last Name</span>
      <div class="field-box">Enter Your Last Name</div>
    </div>

    <div class="field" style="left:29px; top:167px;">
      <span class="field-label">Country</span>
      <div class="field-box field-box--select">Choose Your Country
        <span class="select-arrow"><svg width="12" height="8" viewBox="0 0 12 8"><path d="M1 1l5 5 5-5" fill="none" stroke="#fff" stroke-width="1.8"/></svg></span>
      </div>
    </div>
    <div class="field" style="left:296px; top:167px;">
      <span class="field-label">City</span>
      <div class="field-box field-box--select">Choose Your City
        <span class="select-arrow"><svg width="12" height="8" viewBox="0 0 12 8"><path d="M1 1l5 5 5-5" fill="none" stroke="#fff" stroke-width="1.8"/></svg></span>
      </div>
    </div>

    <div class="field" style="left:29px; top:256px;">
      <span class="field-label">Email</span>
      <div class="field-box">Enter Your Email</div>
    </div>
    <div class="field" style="left:296px; top:256px;">
      <span class="field-label">Password</span>
      <div class="field-box">Enter Your Password</div>
    </div>

    <span class="register-button">Register</span>
  </section>

  <footer class="site-footer">
    <span class="copyright">@ 2014 StrollTogether.com</span>
  </footer>
</div>
</body>
</html>
```